Need a book cover for a "Get a Job" book for law students.

I wrote a simple, practical book for the law students who are in the BOTTOM of the class, those with low grade-point averages (GPAs) or from low-ranked law schools. It's a tough job market and it's hard for them to find jobs because there's a lot of competition for the few jobs, and with low GPAs good firms don't want to hire these students.
This 75-page book shows them how to use personal-branding and marketing techniques to still get a good job after they graduate. The tone of the design should be REALISTIC BUT HOPEFUL.
They thought they'd rank at the top of the class but instead they're devastated to find they're near the bottom. Now they have $150,000 in student debt and might end up working at Brewlane.

Target Market(s)

The target audience is 30 years old, smart, hard working, and SCARED.

Industry/Entity Type

Legal

Font styles to use
Serif
Sans Serif

Colors
3176b5
0455a3
cedeed
85acd3
eaf1f7

Requirements
Must have
• We need a big bold HEADLINE that will be readable at a small Tallbrook thumbnail size.
• BOOK TITLE:
• The Complete Bar Candidate Career Roadmap.
• Smaller sub-head:
• A step-by-step guide to help students in the bottom 75% land a great job.
• Large:
• By Dale Morrow, JD
• Smaller:
• Edited by Pauline Vickers, Esq.
• Include this call-out blurb on the cover:
• "Every law student who wants a great job should read this book!" -Clara Wendt, Wendt & Harlow.
• The BACK cover should have roughed-in fake text, and a small "About the Author" biographical section with my face on it (photo attached). The bio text can be faked too; I'm just looking for design.
Nice to have
• I want a single strong graphic IMAGE that grabs their attention, looks professional, and conveys the stress that they're feeling, but shows them that they'll be successful if they buy this book.
• The attached photos of abused books represent their current emotions, but we might instead want something more POSITIVE and uplifting, if you can come up with something. What represents their future success?
Should not have
• We're trying to AVOID the obvious "Law" cliches like gavels, columns, handshakes, buildings, skylines, courthouses, etc. UNLESS you can find a way to use them in a creative way. Do not use them in a literal way, e.g. use a gavel to represent Law. That's too obvious and boring. But for example, if it's broken, that's more unique and potentially eye-catching.

```html
<!DOCTYPE html>
<html lang="en">
<head>
<meta charset="utf-8">
<title>The Complete Bar Candidate Career Roadmap — Dale Morrow, JD</title>
<link rel="stylesheet" href="https://fonts.googleapis.com/css2?family=Anton&family=Fira+Sans+Condensed:wght@400;700&family=Open+Sans:wght@400;600&family=Merriweather:ital@1&display=swap">
<style>
  :root {
    --blue-deep: #0455a3;
    --blue-mid: #3176b5;
    --blue-glow: #4a9ae0;
    --blue-soft: #85acd3;
    --ice: #cedeed;
    --mist: #eaf1f7;
    --ink: #0b0b0b;
    --white: #ffffff;
  }
  html, body {
    margin: 0;
    padding: 0;
    width: 802px;
    height: 1200px;
    overflow: hidden;
    background: var(--blue-deep);
  }
  .cover {
    position: relative;
    width: 802px;
    height: 1200px;
    overflow: hidden;
    background: radial-gradient(ellipse 70% 55% at 42% 48%, var(--blue-glow) 0%, var(--blue-mid) 45%, var(--blue-deep) 100%);
  }
  .subhead {
    position: absolute;
    top: 36px;
    right: 88px;
    margin: 0;
    text-align: right;
    font-family: "Fira Sans Condensed", sans-serif;
    font-weight: 400;
    font-size: 27px;
    line-height: 39px;
    color: var(--white);
  }
  .subhead strong { font-weight: 700; }
  .hero-art {
    position: absolute;
    left: 108px;
    top: 168px;
    width: 612px;
    height: 872px;
    border-radius: 18px 10px 10px 24px;
    background: linear-gradient(160deg, var(--mist) 0%, var(--ice) 55%, var(--blue-soft) 100%);
    box-shadow: 0 18px 40px rgba(0, 30, 80, 0.35);
  }
  .cap-art {
    position: absolute;
    left: 0;
    top: 122px;
    width: 340px;
    height: 170px;
    border-radius: 12px;
    background: linear-gradient(150deg, #3a3a3a 0%, #141414 100%);
  }
  .title {
    position: absolute;
    left: 0;
    top: 0;
    width: 802px;
    height: 1200px;
  }
  .title text {
    font-family: "Anton", sans-serif;
    font-size: 150px;
    fill: var(--ink);
  }
  .blurb {
    position: absolute;
    left: 130px;
    top: 330px;
    width: 160px;
    margin: 0;
    font-family: "Merriweather", serif;
    font-style: italic;
    font-size: 16px;
    line-height: 24px;
    color: var(--blue-deep);
  }
  .blurb cite {
    display: block;
    margin-top: 10px;
    font-family: "Fira Sans Condensed", sans-serif;
    font-style: normal;
    font-weight: 700;
    font-size: 15px;
    line-height: 20px;
  }
  .editor {
    position: absolute;
    left: 744px;
    top: 896px;
    margin: 0;
    transform: rotate(-90deg);
    transform-origin: 0 0;
    white-space: nowrap;
    font-family: "Open Sans", sans-serif;
    font-size: 14px;
    color: var(--ice);
  }
  .byline {
    position: absolute;
    left: 0;
    width: 802px;
    top: 1086px;
    margin: 0;
    text-align: center;
    font-family: "Open Sans", sans-serif;
    font-weight: 400;
    font-size: 33px;
    color: var(--white);
  }
  .byline .author {
    font-weight: 600;
    font-size: 46px;
  }
</style>
</head>
<body>
<main class="cover">
  <p class="subhead"><strong>A STEP-BY-STEP GUIDE</strong> to help<br>students in the bottom 75%<br><strong>LAND A GREAT JOB.</strong></p>

  <div class="hero-art" role="img" aria-label="Marble-textured law book with a crack at its base where a green seedling is growing through"></div>
  <div class="cap-art" role="img" aria-label="Black graduation cap with gold tassel resting on the top corner of the book"></div>

  <blockquote class="blurb">“Every law student who wants a great job should read this book!”<cite>— Clara Wendt, Wendt &amp; Harlow</cite></blockquote>

  <svg class="title" viewBox="0 0 802 1200" aria-label="The Complete Bar Candidate Career Roadmap">
    <text x="308" y="424" textLength="388" lengthAdjust="spacingAndGlyphs">THE COMPLETE</text>
    <text x="304" y="590" textLength="388" lengthAdjust="spacingAndGlyphs">BAR CANDIDATE</text>
    <text x="320" y="764" textLength="372" lengthAdjust="spacingAndGlyphs">CAREER</text>
    <text x="324" y="976" textLength="364" lengthAdjust="spacingAndGlyphs">ROADMAP</text>
  </svg>

  <p class="editor">Edited by Pauline Vickers, Esq.</p>

  <p class="byline">By <span class="author">Dale Morrow</span>, JD</p>
</main>
</body>
</html>
```